Personal Finance Author needs a postcard

Hi there,

I am a Canadian personal finance author and have published a new book called The Wealth Compass.

I teach Millennials how to create a 6-figure portfolio through investing (https://www.dariafelt.com/)

I'm speaking at some conferences so we were going to print some postcards to hand out to attendees with our info and calls-to-action on them.

I am looking for 4x6 (horizontal) postcard (no space needed for shipping label).

Logos, Headshots and Book Cover:
https://files.cloudvaultex.com/folders/8kQpZrT2mWvN4xLbJ7sHdYc3FgA9eUoRi?usp=sharing

Both sides will be full colour. I would like a clean and simple look. Our main sites are www.DariaFelt.com and www.TheWealthCompassBook.com if you want to get a sense of style and design.
I also uploaded a few marketing materials so you can see the existing designs.

Side 1:
Get Instant Access to your Free Resources - main headline

(small bullets underneath)
- The Wealth Compass Checklist
- Financial Worksheets
- Database of Investment Tools

DariaFelt.com/Resources

At the bottom, include "Don't forget to follow Daria Felt on social media:
Linkedin: @dariafelt7
Facebook: @thewealthcompassbook Instagram: @thewealthcompassbook Twitter: @WealthCompassBk"

Side 2:
Headline - Want to work directly with Daria and The Wealth Compass team to help you make your money grow and stay safe?

Work with us to (bullet point list)...
- Hire Daria as a Keynote Speaker
- Teach Financial Literacy Workshops
- Receive Financial Coaching

Want To Learn More About How We Can Help?
DariaFelt.com/Services

Include my contact info:
Daria Felt
Author | Speaker | Investor
daria@thewealthcompassbook.com
416-555-0187

Target Market(s)

Millennials who want to learn how to save and invest their money. I focus on stock market investing, real estate investing and entrepreneurship.

Industry/Entity Type

Financial Service

Font styles to use
Sans Serif

Colors

Designer to choose colors to be used in the design.

Requirements
Must have
• Photo of Daria Felt
• The Wealth Compass logo
• Green, Gold/Yellow to match existing colours
• modern business style postcard

```html
<!DOCTYPE html>
<html lang="en">
<head>
<meta charset="utf-8">
<title>The Wealth Compass – Postcard</title>
<link rel="stylesheet" href="https://fonts.googleapis.com/css2?family=Arimo:wght@400;700&display=swap">
<style>
  :root {
    --green: #04602f;
    --gold: #ebb83e;
    --ink: #111111;
    --white: #ffffff;
    --line: #9a9a9a;
  }
  * { box-sizing: border-box; margin: 0; padding: 0; }
  html, body { width: 1200px; height: 1200px; overflow: hidden; background: var(--white); }
  body { position: relative; font-family: "Arimo", Arial, sans-serif; color: var(--ink); }

  .postcard { position: absolute; width: 821px; height: 546px; background: var(--white); border: 1px solid var(--line); overflow: hidden; }
  .postcard--front { left: 32px; top: 28px; }
  .postcard--back { left: 338px; top: 622px; }

  /* front */
  .author-name { position: absolute; left: 14px; top: 30px; width: 212px; text-align: center;
    font-size: 27px; font-weight: 700; color: var(--ink); letter-spacing: 0.3px; }
  .brand-name { position: absolute; left: 14px; top: 82px; width: 212px; text-align: center;
    font-size: 36px; font-weight: 700; line-height: 42px; color: var(--green); }
  .book-stack { position: absolute; left: 36px; top: 228px; width: 176px; height: 254px; z-index: 2;
    background: linear-gradient(160deg, #e9ece8 0%, #cfd6cf 45%, #2f6e44 100%); }
  .offer { position: absolute; left: 234px; top: 0; width: 339px; height: 458px; background: var(--gold); }
  .offer__title { position: absolute; left: 20px; top: 86px; font-size: 23px; font-weight: 700;
    color: var(--green); line-height: 27px; text-transform: uppercase; letter-spacing: 0.2px; }
  .checklist { list-style: none; position: absolute; left: 15px; top: 164px; font-size: 20px; line-height: 34.5px; }
  .checklist li, .services li { display: flex; align-items: center; }
  .checklist li::before { content: ""; width: 8px; height: 8px;
    border: 2px solid var(--green); margin-right: 10px; flex: none; }
  .services li::before { content: ""; width: 8px; height: 8px;
    border: 2px solid var(--green); margin-right: 14px; flex: none; }
  .offer__url { position: absolute; left: 0; width: 339px; text-align: center; top: 405px; font-size: 20px; }
  .headshot { position: absolute; left: 573px; top: 0; width: 247px; height: 458px;
    background: linear-gradient(180deg, #f3f3f3 0%, #d9c1ae 25%, #2a2d36 45%, #1e2029 100%); }
  .social { position: absolute; left: 0; top: 458px; width: 100%; height: 88px; background: var(--green);
    color: var(--white); text-align: center; font-size: 18.5px; line-height: 23.5px; padding-top: 9px; }
  .social span { margin: 0 6px; }

  /* back */
  .invite { height: 127px; background: var(--gold); padding: 28px 60px 0 66px;
    font-size: 22px; font-weight: 700; line-height: 27.5px; text-transform: uppercase; }
  .back-body { padding: 31px 0 0 64px; font-size: 20.5px; }
  .back-body p { line-height: 25px; }
  .services { list-style: none; margin-left: 6px; line-height: 25px; }
  .learn { margin-top: 28px; color: var(--green); font-weight: 700; font-size: 22px; text-transform: uppercase; }
  .learn-url { font-weight: 700; font-size: 22px; }
  .contact { margin-top: 27px; line-height: 25px; }
  .contact strong { font-weight: 700; }
  .back-band { position: absolute; left: 0; bottom: 0; width: 100%; height: 51px; background: var(--green); }
</style>
</head>
<body>

<section class="postcard postcard--front">
  <p class="author-name">DARIA FELT</p>
  <p class="brand-name">The<br>Wealth<br>Compass</p>
  <div class="book-stack" role="img" aria-label="Stack of The Wealth Compass books by Daria Felt"></div>

  <div class="offer">
    <h2 class="offer__title">Get instant access to<br>your free resources</h2>
    <ul class="checklist">
      <li>The Wealth Compass Checklist</li>
      <li>Financial Worksheets</li>
      <li>Database of Investment Tools</li>
    </ul>
    <p class="offer__url">DariaFelt.com/Resources</p>
  </div>

  <div class="headshot" role="img" aria-label="Photo of Daria Felt in a dark blazer, hand on hip"></div>

  <footer class="social">
    Don't forget to follow Daria Felt on social media:<br>
    <span>Linkedin: @dariafelt7</span><span>Facebook: @thewealthcompassbook</span><br>
    <span>Instagram: @thewealthcompassbook</span><span>Twitter: @WealthCompassBk</span>
  </footer>
</section>

<section class="postcard postcard--back">
  <h2 class="invite">Want to work directly with Daria and The Wealth Compass team to help you make your money grow and stay safe?</h2>
  <div class="back-body">
    <p>Work with us to :</p>
    <ul class="services">
      <li>Hire Daria as a Keynote Speaker</li>
      <li>Teach Financial Literacy Workshops</li>
      <li>Receive Financial Coaching</li>
    </ul>
    <p class="learn">Want to learn more about how we can help?</p>
    <p class="learn-url">DariaFelt.com/Services</p>
    <p class="contact"><strong>Daria Felt</strong><br>
      Author | Speaker | Investor<br>
      daria@thewealthcompassbook.com<br>
      416-555-0187</p>
  </div>
  <div class="back-band"></div>
</section>

</body>
</html>
```